GravaLoop. Customer needs to know about us, what services we provide & contact us

We are a waste tire recycling company. Our primary focus is on providing a sustainable and cost effective service focusing on: Waste Tire Management, Hassle Free Scheduling for Tire Collection, Mobile Shredding & Special site cleanup services. GravaLoop will be producing TDF, Clean Tire Wire & further materials.
Please look at https://harvonrubber.example
Please look at https://quelbamaterials.example

This is the look and feel of what we want

I have attached a word document with our website info.

Target Market(s)

Tire Install Companies. Such as morbanhaul.example. TDF Purchasers such as pelkofuel.example.

Industry/Entity Type

Waste Tire Recycling

Coding

Coded - Design and coding required

Number of Pages Required

3 page

Font styles to use
Other font styles liked:
• Look at our logo

Requirements
Must have
• We need a 3 page setup for About Us, Services & Contact Us. Contact us should be a form them can fill out and submit to us Images that are related to waste tire recycling. Clean, modern, innovative.
Nice to have
• The color and feel of the website should work with our logo that we did with artpivot
Should not have
• Anything progressive, political or "woke"

```html
<!DOCTYPE html>
<html lang="en">
<head>
<meta charset="utf-8">
<title>GravaLoop – Waste Tire Recycling</title>
<link rel="stylesheet" href="https://fonts.googleapis.com/css2?family=Poppins:wght@400;500;600;700;800&family=Roboto+Condensed:wght@700&display=swap">
<style>
:root{
  --green:#16913d;
  --green-dark:#0f7a31;
  --ink:#222;
  --text:#444;
  --light:#f3f3f3;
  --white:#fff;
  --navy:#1e2a3f;
  --footer-bar:#0d0d0d;
}
*{box-sizing:border-box;margin:0;padding:0}
html,body{width:1200px;height:4584px;overflow:hidden}
body{position:relative;font-family:'Poppins',sans-serif;color:var(--text);background:var(--white)}
.abs{position:absolute}
.heading{font-family:'Roboto Condensed',sans-serif;font-weight:700;font-size:32px;color:var(--ink);display:flex;align-items:center;gap:8px}
.heading .accent{color:var(--green)}
.heading .dot{width:28px;height:28px;border-radius:50%;background:var(--green)}
.body-text{font-size:13.5px;line-height:24.5px;letter-spacing:.3px}
.body-text p{margin-bottom:4px}
.body-text b{color:var(--green);font-weight:700}
.btn{display:inline-block;background:var(--green);color:var(--white);font-size:14px;padding:10px 20px;text-decoration:none}
.hero{left:0;top:0;width:1200px;height:590px;background:linear-gradient(180deg,#5b5f62 0%,#3a3d40 45%,#3b5a7a 80%,#2f4661 100%)}
.brand{font-weight:800;font-size:34px;color:var(--white);letter-spacing:-.5px}
.topbar{right:162px;top:24px;display:flex;gap:24px;color:var(--white);font-size:14px;align-items:center}
.topbar span{display:flex;gap:8px;align-items:center}
.nav{right:162px;top:60px;display:flex;gap:42px;font-size:14px;color:var(--white)}
.hero-title{left:0;width:1200px;top:182px;text-align:center;font-weight:700;font-size:27px;line-height:36px;color:var(--white)}
.hero-btn{left:540px;top:268px}
.card{background:var(--white);width:426px;height:206px;padding:30px 34px}
.card .icon{width:44px;height:44px;border-radius:50%;background:var(--green);margin-bottom:8px;position:relative}
.card .icon::after{content:"";position:absolute;right:-12px;top:-6px;width:24px;height:24px;border-radius:50%;background:#222;border:2px solid #fff}
.card h3{font-size:15.5px;font-weight:500;color:var(--ink);margin-bottom:8px}
.card p{font-size:13.5px;line-height:22px;letter-spacing:.6px}
.card p a{color:var(--green);font-weight:700;text-decoration:none;margin-left:8px}
.contact-box{background:rgba(255,255,255,.15);width:267px;height:97px;display:flex;align-items:center;gap:18px;padding:0 26px;color:var(--white);font-size:13px;line-height:19px;white-space:nowrap}
</style>
</head>
<body>

<div class="abs hero" role="img" aria-label="Photo of scrap tires piled in a blue dumpster container"></div>
<svg class="abs" style="left:0;top:355px" width="1200" height="240" viewBox="0 0 1200 240"><polygon points="0,180 1200,0 1200,240 0,240" fill="#fff"/><polygon points="0,205 1200,25 1200,60 0,240" fill="#16913d" opacity=".85"/></svg>
<div class="abs brand" style="left:162px;top:36px">GravaLoop</div>
<div class="abs topbar">
  <span><svg width="20" height="14" viewBox="0 0 20 14"><rect x="1" y="1" width="18" height="12" fill="none" stroke="#fff" stroke-width="1.5"/><path d="M1 1l9 7 9-7" fill="none" stroke="#fff" stroke-width="1.5"/></svg>info@gravaloop.example</span>
  <span><svg width="16" height="16" viewBox="0 0 24 24"><path d="M6.6 10.8a15 15 0 006.6 6.6l2.2-2.2a1 1 0 011-.25 11.4 11.4 0 003.6.6 1 1 0 011 1V20a1 1 0 01-1 1A17 17 0 013 4a1 1 0 011-1h3.5a1 1 0 011 1 11.4 11.4 0 00.6 3.6 1 1 0 01-.25 1z" fill="#fff"/></svg>555-204-3187</span>
</div>
<div class="abs nav"><span>Home</span><span>About</span><span>Services</span><span>Contact Us</span></div>
<h1 class="abs hero-title">We Are A Waste Tire Recycling Company,<br>Providing A Sustainable And Cost Effective Service</h1>
<a class="abs btn hero-btn" href="#contact">Contact Us</a>

<h2 class="abs heading" style="left:162px;top:640px"><span class="dot"></span>About <span class="accent">GravaLoop</span></h2>
<div class="abs body-text" style="left:162px;top:696px;width:434px">
  <p>GravaLoop is forging the way towards a more sustainable future through scrap tire collection &amp; waste tire recycling. You've got a business to run, and we've got you covered. Let us worry about your <b>scrap tire removal</b> so you don't have to. Through the use of innovative technologies, we are not only more eco-friendly but able to pass the savings along to our customers.</p>
  <p>Waste Tire Management is a global problem that GravaLoop aims to resolve. Through our innovative approach to <b>waste tire management</b>, we are focused on resolving environmental concerns head-on. All while giving businesses across the region an opportunity to make a difference for the environment and their bottom line.</p>
</div>
<div class="abs" style="left:652px;top:644px;width:219px;height:186px;background:linear-gradient(135deg,#777,#222)" role="img" aria-label="Photo of stacked black tires"></div>
<div class="abs" style="left:820px;top:838px;width:218px;height:186px;background:linear-gradient(135deg,#c9ccd0,#56585c)" role="img" aria-label="Photo of a worker in a tire warehouse"></div>
<div class="abs" style="left:796px;top:785px;width:96px;height:96px;border-radius:50%;background:var(--green);border:5px solid #fff"></div>

<div class="abs" style="left:160px;top:1098px;width:385px;height:365px;background:linear-gradient(180deg,#b9cde0,#c98a4a 60%,#3d3b36)" role="img" aria-label="Illustration of a recycling loop filled with factory and sky scenes around a green leaf"></div>
<div class="abs body-text" style="left:596px;top:1064px;width:442px;font-size:13px;line-height:24px">
  <p>Built upon a foundation of innovation, attention to detail, and budget-conscious services, GravaLoop is at the forefront of pushing the boundaries of what can be achieved through advancing technology. Through our rigorous processes, environmental commitment we go beyond expectations. GravaLoop aims to achieve efficiency all while revolutionizing the industry.</p>
  <p>When your company is deciding on <b>used-tire disposal</b> responsibilities you can rest assured that GravaLoop has your company's interest at its core. Leave the costly equipment, manpower, and output-reducing duties to us. GravaLoop will help you focus your time where it counts.</p>
  <p>At our heart GravaLoop's focus is to always better our processes, support our industry, and environment. Here at GravaLoop we see ourselves as an extension of your team, outdoing competitors on speed, value, and price point.</p>
  <p style="color:var(--ink);font-weight:600">Here at GravaLoop we're making a stand. <b>Are you joining us</b></p>
</div>

<div class="abs" style="left:0;top:1549px;width:1200px;height:694px;background:linear-gradient(160deg,#7a4a2e,#3b3a3a 40%,#2a2d30 100%)" role="img" aria-label="Photo of a field of discarded tires"></div>
<h2 class="abs heading" style="left:0;width:1200px;top:1634px;justify-content:center;color:#fff"><span class="dot" style="background:#fff"></span>Our Services</h2>
<div class="abs card" style="left:162px;top:1714px"><div class="icon"></div><h3>Waste Tire Management &amp; Recycling</h3><p>Our priority is our core focus on providing our clients with industry leading waste tire management services. <a href="#">Read More...</a></p></div>
<div class="abs card" style="left:612px;top:1714px"><div class="icon"></div><h3>Tire Remediation &amp; Special Tire Clean-Ups</h3><p>GravaLoop's core business was derived from our handling of special tire clean up situations. These abandoned or <a href="#">Read More...</a></p></div>
<div class="abs card" style="left:162px;top:1946px"><div class="icon"></div><h3>Scheduling &amp; Billing</h3><p>GravaLoop is here to make your day-to-day easier with a seamless scheduling program. We pride ourselves <a href="#">Read More...</a></p></div>
<div class="abs card" style="left:612px;top:1946px"><div class="icon"></div><h3>First Rate Customer Support &amp; Service</h3><p>At GravaLoop our customer is our priority. We have built a team that shares in our commitment to excellence and <a href="#">Read More...</a></p></div>

<h2 class="abs heading" style="left:0;width:1200px;top:2319px;justify-content:center"><span class="dot"></span><span class="accent">Clients Review</span></h2>
<div class="abs" style="left:251px;top:2408px;width:219px;height:219px;background:#3a3a3a;padding:14px"><div style="width:100%;height:100%;background:linear-gradient(180deg,#ddd,#b89a84)" role="img" aria-label="Portrait photo of the reviewing client"></div></div>
<div class="abs" style="left:262px;top:2388px;font-family:Georgia,serif;font-size:110px;line-height:1;color:var(--green);font-weight:700">&ldquo;</div>
<p class="abs body-text" style="left:513px;top:2402px;width:450px;font-size:13.5px">Lorem ipsum dolor sit amet, consectetuer adipiscing elit, sed diam nonummy nibh euismod tincidunt ut laoreet dolore magna aliquam erat volutpat. Ut wisi enim ad minim veniam, quis nostrud exerci tation ullamcorper suscipit lobortis nisl ut aliquip ex ea commodo consequat.</p>
<p class="abs" style="left:513px;top:2546px;font-size:13.5px"><b style="color:var(--ink)">Dale Maren</b>&nbsp;&nbsp; Lorem ipsum dolor</p>
<svg class="abs" style="left:511px;top:2605px" width="80" height="20" viewBox="0 0 80 20"><path d="M28 10H4m8-7l-8 7 8 7" fill="none" stroke="#aaa" stroke-width="1.5"/><path d="M50 10h24m-8-7l8 7-8 7" fill="none" stroke="#16913d" stroke-width="1.5"/></svg>

<div class="abs" style="left:0;top:2727px;width:1200px;height:520px;background:var(--light)"></div>
<h2 class="abs heading" style="left:162px;top:2812px"><span class="dot"></span><span class="accent">Our Product</span></h2>
<p class="abs body-text" style="left:162px;top:2866px;width:434px">TDF: GravaLoop seeks to be one of the leading TDF suppliers to the region. This is a product with a wide range of demand from pulp and paper mills, electrical utilities, industrial boilers to cement and asphalt plants our expertly handled tire-derived fuel is being used and receiving high marks for its ever-expanding list of benefits. From driving boiler efficiency to stamping out emissions, GravaLoop wants to be your TDF supplier offering additional services to include tire pick-up to TDF drop-off we have your back!</p>
<a class="abs btn" style="left:162px;top:3117px" href="#contact">Contact Us</a>
<div class="abs" style="left:652px;top:2818px;width:386px;height:338px;background:linear-gradient(180deg,#6b7a4e,#3a3b36 40%,#1f1f1f)" role="img" aria-label="Photo of a heap of shredded tire-derived fuel"></div>

<div class="abs" style="left:0;top:3247px;width:1200px;height:306px;background:linear-gradient(180deg,#2a3a55,#1b2334 60%,#10141c)" role="img" aria-label="Photo of a lone tree reflected in a lake at night"></div>
<div class="abs" style="left:0;width:1200px;top:3326px;text-align:center;font-family:'Roboto Condensed',sans-serif;font-weight:700;color:#fff">
  <div style="font-size:31px">GravaLoop Is Committed To</div>
  <div style="font-size:22px;margin-top:6px">Sustainability And Looking At Your Waste Tires As A Means To Offer Innovation</div>
</div>
<a class="abs btn" style="left:540px;top:3428px" href="#contact">Contact Us</a>

<div class="abs" style="left:851px;top:3694px;width:349px;height:347px;background:radial-gradient(ellipse at center,#e6e6e6,#fff 72%)" role="img" aria-label="Faded image of stacked tires"></div>
<div class="abs" style="left:160px;top:3706px;font-family:'Roboto Condensed',sans-serif;font-weight:700;font-size:114px;color:var(--green);line-height:1">300,000,000</div>
<div class="abs" style="left:162px;top:3826px;font-family:'Roboto Condensed',sans-serif;font-weight:700;font-size:26px;color:var(--ink)">Scrap Tires Are Generated Annually By GravaLoop</div>
<p class="abs body-text" style="left:162px;top:3884px;width:570px">Lorem ipsum dolor sit amet, consectetuer adipiscing elit, sed diam nonummy nibh euismod tincidunt ut laoreet dolore magna aliquam erat volutpat. Ut wisi enim ad minim veniam, quis nostrud exerci tation ullamcorper suscipit lobortis nisl ut aliquip ex ea commodo consequat.</p>
<a class="abs btn" style="left:162px;top:4003px" href="#contact">Contact Us</a>

<svg class="abs" style="left:0;top:4080px" width="1200" height="462" viewBox="0 0 1200 462"><polygon points="0,192 1200,14 1200,462 0,462" fill="#16913d"/><polygon points="0,178 1200,0 1200,14 0,192" fill="#bbb"/></svg>
<div class="abs brand" style="left:0;width:1200px;top:4278px;text-align:center">GravaLoop</div>
<div class="abs" style="left:0;width:1200px;top:4364px;display:flex;justify-content:center;gap:60px;font-size:14px;color:#fff"><span>Home</span><span>About</span><span>Services</span><span>Contact Us</span></div>
<div class="abs contact-box" id="contact" style="left:162px;top:4414px">
  <svg width="40" height="40" viewBox="0 0 40 40" fill="none" stroke="#fff" stroke-width="1.5"><circle cx="20" cy="20" r="17"/><ellipse cx="20" cy="20" rx="7" ry="17"/><path d="M3 20h34"/></svg>
  <span>48 Cinder Mill Rd<br>Ashford, ST 40512</span></div>
<div class="abs contact-box" style="left:466px;top:4414px">
  <svg width="40" height="40" viewBox="0 0 24 24" fill="none" stroke="#fff" stroke-width="1"><path d="M6.6 10.8a15 15 0 006.6 6.6l2.2-2.2a1 1 0 011-.25 11.4 11.4 0 003.6.6 1 1 0 011 1V20a1 1 0 01-1 1A17 17 0 013 4a1 1 0 011-1h3.5a1 1 0 011 1 11.4 11.4 0 00.6 3.6 1 1 0 01-.25 1z"/></svg>
  <span><b>Phone</b><br>555-204-3187</span></div>
<div class="abs contact-box" style="left:771px;top:4414px">
  <svg width="40" height="40" viewBox="0 0 40 40" fill="none" stroke="#fff" stroke-width="1.5"><rect x="4" y="10" width="32" height="22"/><path d="M4 10l16 12 16-12"/></svg>
  <span><b>Email</b><br>info@gravaloop.example</span></div>
<div class="abs" style="left:0;top:4541px;width:1200px;height:43px;background:var(--footer-bar);color:#fff;font-size:12.5px;padding:13px 162px">© 2022 GravaLoop. All Rights Reserved.</div>
<div class="abs" style="left:918px;top:4556px;display:flex;gap:38px"><span style="width:12px;height:12px;border-radius:50%;background:#fff;display:block"></span><span style="width:12px;height:12px;border-radius:50%;background:#fff;display:block"></span><span style="width:12px;height:12px;border-radius:50%;background:#fff;display:block"></span></div>

</body>
</html>
```